Business card - mobile service

O KiraTel is a mobile family safety service based on tablets and smartphones.
The business card must have:
BASIC INFO
Company Logo
Name
Position / Job Title: Co-founder
Mobile Phone Number: +55 (11) 5080 6172
Land Line: +55 (11) 9087 614352
Email Address: name@kiratel-example.com
Web Site URL: www.kiratel-example.com
PROMOTIONAL INFO
Try KiraTel free Today!
Your personal promo code: xxxx-2222-uuuu-7777-1234
Promo code text explanation with the instructions about the trial offer
Updates
Dears,
One more must have: the KiraTel slogan:
Industry/Entity Type
Safety
Look and feel
Each slider illustrates characteristics of the customer's brand and the style your logo design should communicate.

```html
<!DOCTYPE html>
<html lang="en">
<head>
<meta charset="utf-8">
<title>KiraTel business card</title>
<link href="https://fonts.googleapis.com/css2?family=Open+Sans:wght@400;600;700&display=swap" rel="stylesheet">
<style>
  :root {
    --backdrop: #d9d9d9;
    --card-white: #ffffff;
    --brand-blue: #2ea8df;
    --brand-yellow: #f9c33c;
    --ink: #222222;
    --on-blue: #ffffff;
  }
  * { margin: 0; padding: 0; box-sizing: border-box; }
  html, body {
    width: 1200px;
    height: 900px;
    overflow: hidden;
    background: var(--backdrop);
    font-family: "Open Sans", Arial, sans-serif;
  }
  .stage {
    position: relative;
    width: 1200px;
    height: 900px;
  }
  .card {
    position: absolute;
    top: 304px;
    width: 492px;
    height: 290px;
    overflow: hidden;
    box-shadow: 0 2px 6px rgba(0,0,0,0.18);
  }
  .card--front { left: 94px; background: var(--card-white); color: var(--ink); }
  .card--back { left: 612px; background: var(--brand-blue); color: var(--on-blue); }

  .brand-name {
    font-weight: 700;
    letter-spacing: -0.5px;
    line-height: 1;
  }
  .card--front .brand-name {
    position: absolute;
    left: 42px;
    top: 30px;
    font-size: 30px;
    color: var(--brand-blue);
  }
  .holder {
    position: absolute;
    left: 42px;
    top: 114px;
  }
  .holder__name {
    font-size: 21px;
    font-weight: 700;
    color: var(--brand-blue);
    line-height: 1.2;
  }
  .holder__role {
    font-size: 13px;
    line-height: 1.4;
  }
  .contacts {
    position: absolute;
    left: 42px;
    top: 168px;
    list-style: none;
    font-size: 13px;
    line-height: 20px;
  }
  .contacts__label {
    color: var(--brand-yellow);
    font-weight: 600;
    display: inline-block;
    width: 12px;
  }
  .website {
    position: absolute;
    left: 42px;
    top: 236px;
    font-size: 13px;
  }

  .card--back .promo-block {
    position: absolute;
    right: 26px;
    top: 44px;
    text-align: right;
  }
  .card--back .brand-name {
    font-size: 44px;
    color: var(--on-blue);
  }
  .slogan {
    margin-top: 6px;
    font-size: 15px;
    font-weight: 600;
  }
  .offer {
    position: absolute;
    right: 26px;
    top: 152px;
    text-align: right;
  }
  .offer__title {
    font-size: 15px;
    font-weight: 700;
    margin-bottom: 6px;
  }
  .offer__line {
    font-size: 13px;
    line-height: 22px;
  }
</style>
</head>
<body>
<main class="stage">
  <section class="card card--front" aria-label="Card front">
    <div class="brand-name">kiratel</div>
    <div class="holder">
      <p class="holder__name">Rina Solano</p>
      <p class="holder__role">Co-founder</p>
    </div>
    <ul class="contacts">
      <li><span class="contacts__label">M</span> +55 (11) 5080 6172</li>
      <li><span class="contacts__label">T</span> +55 (11) 9087 614352</li>
      <li><span class="contacts__label">E</span> name@kiratel-example.com</li>
    </ul>
    <p class="website">www.kiratel-example.com</p>
  </section>

  <section class="card card--back" aria-label="Card back">
    <div class="promo-block">
      <div class="brand-name">kiratel</div>
      <p class="slogan">Your Family Safety Service</p>
    </div>
    <div class="offer">
      <p class="offer__title">Try KiraTel free Today!</p>
      <p class="offer__line">Your personal promo code:</p>
      <p class="offer__line">xxxx-2222-uuuu-7777-1234</p>
      <p class="offer__line">Promo code text explanation with</p>
      <p class="offer__line">the instructions about the trial offer.</p>
    </div>
  </section>
</main>
</body>
</html>
```